Long term design collaboration - mobile app design & web app design

We are looking for a talented mobile designer to help us improve our UI & UX for mobile app and web app.

The screens that need to be redesigned are attached.

There is potentially a lot more work in future design available for the successful candidate.
The successful candidate would have to take part in daily stand-up around 3 times per week.
The successful candidate would join a dev team
We are software company that does property management

```html
<!DOCTYPE html>
<html lang="en">
<head>
<meta charset="utf-8">
<title>Property Management App – Screens</title>
<link rel="stylesheet" href="https://fonts.googleapis.com/css2?family=Poppins:wght@300;400;500;600;700&display=swap">
<style>
  :root{
    --backdrop:#616161;
    --screen-top:#e9f5fc;
    --screen-bottom:#f3f9fd;
    --screen-flat:#edf7fd;
    --navy:#1d5580;
    --ink:#161b21;
    --muted:#5b6670;
    --tab-idle:#cfd7dc;
    --white:#ffffff;
    --alert:#e02424;
    --warn:#f2b705;
  }
  *{box-sizing:border-box;margin:0;padding:0}
  html,body{width:1200px;height:1000px;overflow:hidden;background:var(--backdrop)}
  body{font-family:"Poppins",sans-serif;color:var(--ink)}
  .stage{position:relative;width:2100px;height:1750px;transform:scale(0.571429);transform-origin:0 0}

  .screen{position:absolute;width:322px;background:linear-gradient(180deg,var(--screen-top),var(--screen-bottom));box-shadow:0 10px 28px rgba(0,0,0,.28)}
  .screen-header{position:absolute;left:18px;top:32px;width:340px;display:flex;align-items:center;gap:19px;color:var(--navy);font-size:22px;font-weight:500;white-space:nowrap;line-height:30px}
  .screen-header svg{flex:none;width:18px;height:28px}

  .tab{position:absolute;width:101px;height:101px;border-radius:14px;background:var(--tab-idle);display:flex;flex-direction:column;align-items:center;justify-content:flex-start;padding-top:12px;color:var(--white);font-size:15px;font-weight:300;box-shadow:0 2px 6px rgba(0,0,0,.12)}
  .tab.active{background:var(--navy);font-weight:400}
  .tab svg{width:62px;height:58px;margin-bottom:3px}

  .card{position:absolute;width:269px;border:2px solid var(--navy);border-radius:14px;background:transparent}
  .card-label{position:absolute;top:-17px;left:50%;transform:translateX(-50%);background:var(--screen-flat);padding:0 12px;color:var(--navy);font-size:22px;font-weight:500;white-space:nowrap;line-height:30px}
  .alert-dot{position:absolute;top:-4px;right:-2px;width:13px;height:13px;border:1.5px solid var(--alert);border-radius:50%;color:var(--alert);font-size:9px;line-height:10px;text-align:center;font-weight:600;background:var(--screen-flat)}
  .collapsed-bar{position:absolute;left:16px;right:16px;top:22px;height:20px;border-radius:8px;background:var(--white)}
  .chev-toggle{position:absolute;left:50%;transform:translateX(-50%);width:22px;height:14px}

  .detail-list{position:absolute;left:0;right:0;display:flex;flex-direction:column;align-items:center;text-align:center}
  .detail{margin-bottom:17px;display:flex;flex-direction:column;align-items:center}
  .detail-title{position:relative;font-size:22px;font-weight:500;line-height:30px;display:flex;align-items:center;gap:8px;white-space:nowrap}
  .detail-title .go{width:10px;height:18px}
  .detail-sub{margin-top:5px;font-size:14px;color:var(--muted);line-height:17px}
  .flag{position:absolute;left:-12px;top:-4px;width:13px;height:13px;border-radius:50%;font-size:9px;line-height:10px;text-align:center;font-weight:600}
  .flag.warn{border:1.5px solid var(--warn);color:var(--warn)}
  .flag.alert{border:1.5px solid var(--alert);color:var(--alert)}

  .navy-foot{position:absolute;left:-2px;right:-2px;bottom:-2px;background:var(--navy);border-radius:0 0 14px 14px}
  .white-top{position:absolute;left:0;right:0;top:0;background:var(--white);border-radius:12px 12px 0 0}

  .input-field{position:absolute;left:12px;right:12px;top:26px;height:36px;background:var(--white);border-radius:8px;font-size:14px;color:var(--navy);padding:8px 12px;box-shadow:0 1px 3px rgba(0,0,0,.08)}
  .insurance-types{position:absolute;left:0;right:0;top:88px;color:var(--white);font-size:15px;text-align:center;line-height:21px;font-weight:300;white-space:nowrap}
  .insurance-types span{margin:0 5px}

  .question{position:absolute;left:0;right:0;text-align:center;font-size:22px;font-weight:500;white-space:nowrap}
  .choice{position:absolute;top:62px;width:106px;height:34px;background:var(--white);border-radius:7px;font-size:14px;color:var(--muted);text-align:center;line-height:34px;box-shadow:0 1px 3px rgba(0,0,0,.08)}

  .amount{position:absolute;left:0;right:0;text-align:center;font-size:35px;font-weight:700;line-height:40px}
  .amount-note{position:absolute;left:0;right:0;text-align:center;font-size:15px;color:var(--muted);display:flex;justify-content:center;align-items:center;gap:8px;white-space:nowrap}
  .on-navy{color:var(--white)}
  .amount-note svg{width:10px;height:18px}

  .check-row{position:absolute;left:14px;right:12px;display:flex;align-items:flex-start;gap:12px;color:var(--white);font-size:15px;line-height:17px;font-weight:300}
  .check-box{flex:none;width:35px;height:34px;background:var(--white);border-radius:6px;display:flex;align-items:center;justify-content:center}
  .check-box svg{width:28px;height:28px}
  .check-row span{padding-top:8px}

  .next-btn{position:absolute;left:26px;width:270px;height:54px;background:var(--white);border-radius:8px;color:var(--navy);font-size:23px;font-weight:700;text-align:center;line-height:54px;box-shadow:0 2px 6px rgba(0,0,0,.08)}
</style>
</head>
<body>
<svg width="0" height="0" style="position:absolute">
  <defs>
    <symbol id="i-back" viewBox="0 0 18 28"><path d="M14 3 L4 14 L14 25" fill="none" stroke="currentColor" stroke-width="3" stroke-linecap="round" stroke-linejoin="round"/></symbol>
    <symbol id="i-go" viewBox="0 0 10 18"><path d="M2 2 L8 9 L2 16" fill="none" stroke="currentColor" stroke-width="1.6" stroke-linecap="round" stroke-linejoin="round"/></symbol>
    <symbol id="i-down" viewBox="0 0 22 14"><path d="M3 3 L11 11 L19 3" fill="none" stroke="currentColor" stroke-width="2.4" stroke-linecap="round" stroke-linejoin="round"/></symbol>
    <symbol id="i-up" viewBox="0 0 22 14"><path d="M3 11 L11 3 L19 11" fill="none" stroke="currentColor" stroke-width="2.4" stroke-linecap="round" stroke-linejoin="round"/></symbol>
    <symbol id="i-home" viewBox="0 0 62 58"><g fill="none" stroke="currentColor" stroke-width="3.5" stroke-linejoin="round"><path d="M4 28 L31 4 L58 28"/><path d="M11 22 V54 H51 V22"/><path d="M24 54 V36 H38 V54"/></g></symbol>
    <symbol id="i-overview" viewBox="0 0 62 58"><g fill="none" stroke="currentColor" stroke-width="3.5" stroke-linejoin="round" stroke-linecap="round"><path d="M4 28 L31 4 L58 28"/><path d="M11 22 V54 H40"/><path d="M51 22 V36"/><circle cx="31" cy="33" r="11"/><path d="M39 41 L50 53"/></g></symbol>
    <symbol id="i-finances" viewBox="0 0 62 58"><g fill="none" stroke="currentColor" stroke-width="3"><ellipse cx="22" cy="8" rx="15" ry="5"/><path d="M7 8 V44 C7 50 37 50 37 44 V8"/><path d="M7 17 C7 23 37 23 37 17"/><path d="M7 26 C7 32 37 32 37 26"/><path d="M7 35 C7 41 37 41 37 35"/><circle cx="46" cy="40" r="13"/><path d="M50 33 H44 C40 33 40 40 44 40 H48 C52 40 52 47 48 47 H42 M46 30 V50" stroke-width="2.5"/></g></symbol>
    <symbol id="i-mail" viewBox="0 0 62 58"><g fill="none" stroke="currentColor" stroke-width="3.5" stroke-linejoin="round"><rect x="6" y="10" width="50" height="36"/><path d="M6 10 L31 32 L56 10"/><path d="M6 46 L24 27 M56 46 L38 27"/></g></symbol>
  </defs>
</svg>

<div class="stage">

  <!-- Screen: development overview, collapsed -->
  <section class="screen" style="left:283px;top:62px;height:703px">
    <header class="screen-header"><svg><use href="#i-back"/></svg>Development Overview</header>
  </section>
  <nav>
    <div class="tab active" style="left:310px;top:155px"><svg><use href="#i-home"/></svg>Home</div>
    <div class="tab" style="left:420px;top:155px"><svg><use href="#i-overview"/></svg>Overview</div>
    <div class="tab" style="left:530px;top:155px"><svg><use href="#i-finances"/></svg>Finances</div>
    <div class="tab" style="left:641px;top:155px"><svg><use href="#i-mail"/></svg>Messages</div>
  </nav>
  <div class="card" style="left:310px;top:286px;height:54px"><span class="card-label">General</span><div class="collapsed-bar"></div><svg class="chev-toggle" style="top:25px;color:var(--navy)"><use href="#i-down"/></svg></div>
  <div class="card" style="left:310px;top:368px;height:54px"><span class="card-label">Compliance<span class="alert-dot">!</span></span><svg class="chev-toggle" style="top:25px;color:var(--navy)"><use href="#i-down"/></svg></div>
  <div class="card" style="left:310px;top:450px;height:54px"><span class="card-label">Insurances</span><svg class="chev-toggle" style="top:25px;color:var(--navy)"><use href="#i-down"/></svg></div>
  <div class="card" style="left:310px;top:532px;height:54px"><span class="card-label">Service Charge</span><div class="collapsed-bar"></div><svg class="chev-toggle" style="top:25px;color:var(--navy)"><use href="#i-down"/></svg></div>
  <div class="card" style="left:310px;top:614px;height:54px"><span class="card-label">Cosec</span><div class="collapsed-bar"></div><svg class="chev-toggle" style="top:25px;color:var(--navy)"><use href="#i-down"/></svg></div>

  <!-- Screen: development overview, expanded -->
  <section class="screen" style="left:816px;top:62px;height:1626px">
    <header class="screen-header"><svg><use href="#i-back"/></svg>Development Overview</header>
  </section>
  <nav>
    <div class="tab active" style="left:842px;top:155px"><svg><use href="#i-home"/></svg>Home</div>
    <div class="tab" style="left:953px;top:155px"><svg><use href="#i-overview"/></svg>Overview</div>
    <div class="tab" style="left:1063px;top:155px"><svg><use href="#i-finances"/></svg>Finances</div>
    <div class="tab" style="left:1174px;top:155px"><svg><use href="#i-mail"/></svg>Messages</div>
  </nav>

  <div class="card" style="left:842px;top:286px;height:361px">
    <div class="white-top" style="height:320px"></div>
    <span class="card-label">General</span>
    <div class="detail-list" style="top:30px">
      <div class="detail"><div class="detail-title">Handover Date<svg class="go"><use href="#i-go"/></svg></div><div class="detail-sub">12 January 2023</div></div>
      <div class="detail"><div class="detail-title">Units<svg class="go"><use href="#i-go"/></svg></div><div class="detail-sub">85</div></div>
      <div class="detail" style="margin-bottom:21px"><div class="detail-title">Address<svg class="go"><use href="#i-go"/></svg></div><div class="detail-sub">24 Alder Grove Road,<br>London, N4 7QT</div></div>
      <div class="detail"><div class="detail-title">Section 20 Limit<svg class="go"><use href="#i-go"/></svg></div><div class="detail-sub">£20</div></div>
    </div>
    <div class="navy-foot" style="height:40px"><svg class="chev-toggle" style="top:12px;color:var(--white)"><use href="#i-up"/></svg></div>
  </div>

  <div class="card" style="left:842px;top:676px;height:406px">
    <div class="white-top" style="height:366px"></div>
    <span class="card-label">Compliance<span class="alert-dot">!</span></span>
    <div class="detail-list" style="top:27px">
      <div class="detail"><div class="detail-title">Asbestos<svg class="go"><use href="#i-go"/></svg></div><div class="detail-sub">NA</div></div>
      <div class="detail"><div class="detail-title"><span class="flag warn">?</span>EICR<svg class="go"><use href="#i-go"/></svg></div><div class="detail-sub">-</div></div>
      <div class="detail"><div class="detail-title"><span class="flag alert">!</span>Drains<svg class="go"><use href="#i-go"/></svg></div><div class="detail-sub">Overdue 10 December 2023</div></div>
      <div class="detail"><div class="detail-title"><span class="flag warn">?</span>Gutters<svg class="go"><use href="#i-go"/></svg></div><div class="detail-sub">-</div></div>
      <div class="detail"><div class="detail-title"><span class="flag warn">?</span>Dry Riser<svg class="go"><use href="#i-go"/></svg></div><div class="detail-sub">-</div></div>
    </div>
    <div class="navy-foot" style="height:40px"><svg class="chev-toggle" style="top:12px;color:var(--white)"><use href="#i-up"/></svg></div>
  </div>

  <div class="card" style="left:842px;top:1110px;height:150px">
    <span class="card-label">Insurances</span>
    <div class="input-field">NA</div>
    <div class="navy-foot" style="height:76px"></div>
    <div class="insurance-types"><span>Terrorism</span><span>Buildings</span><span>Engineering</span><br><span>D &amp; O</span><span>Reinstatemen</span></div>
  </div>

  <div class="card" style="left:842px;top:1288px;height:201px">
    <span class="card-label">Service Charge</span>
    <div class="detail-list" style="top:33px">
      <div class="detail"><div class="detail-title">Year End<svg class="go"><use href="#i-go"/></svg></div><div class="detail-sub">12/12/2024</div></div>
      <div class="detail"><div class="detail-title">Demand Dates<svg class="go"><use href="#i-go"/></svg></div><div class="detail-sub">NA</div></div>
    </div>
    <svg class="chev-toggle" style="top:174px;color:var(--navy)"><use href="#i-up"/></svg>
  </div>

  <div class="card" style="left:842px;top:1519px;height:120px">
    <span class="card-label">Cosec</span>
    <div class="question" style="top:26px">Are We Responsible?</div>
    <div class="choice" style="left:22px">Yes</div>
    <div class="choice" style="left:137px">No</div>
  </div>

  <!-- Screen: finances -->
  <section class="screen" style="left:1541px;top:62px;height:703px">
    <header class="screen-header"><svg><use href="#i-back"/></svg>Finances</header>
  </section>
  <nav>
    <div class="tab" style="left:1348px;top:155px"><svg><use href="#i-home"/></svg>Home</div>
    <div class="tab" style="left:1458px;top:155px"><svg><use href="#i-overview"/></svg>Overview</div>
    <div class="tab active" style="left:1568px;top:155px"><svg><use href="#i-finances"/></svg>Finances</div>
    <div class="tab" style="left:1678px;top:155px"><svg><use href="#i-mail"/></svg>Messages</div>
  </nav>

  <div class="card" style="left:1568px;top:286px;height:250px">
    <div class="navy-foot" style="height:130px"></div>
    <div class="white-top" style="height:120px;border-radius:12px"></div>
    <span class="card-label">Receivable</span>
    <div class="amount" style="top:35px">£7,268.22</div>
    <div class="amount-note" style="top:80px">5 Bill(s) Arrears Total<svg><use href="#i-go"/></svg></div>
    <div class="amount on-navy" style="top:140px">£7,268.22</div>
    <div class="amount-note on-navy" style="top:185px">5 Receipt(s) Unallocated Total<svg><use href="#i-go"/></svg></div>
  </div>

  <div class="card" style="left:1568px;top:564px;height:165px">
    <span class="card-label">Payable</span>
    <div class="amount" style="top:43px">£4,268.78</div>
    <div class="amount-note" style="top:88px">5 Invoice(s) Total<svg><use href="#i-go"/></svg></div>
  </div>

  <!-- Screen: legionellas question -->
  <section class="screen" style="left:1543px;top:908px;height:702px">
    <header class="screen-header"><svg><use href="#i-back"/></svg>Legionellas</header>

    <div class="card" style="left:27px;top:99px;height:310px;overflow:hidden">
      <div class="navy-foot" style="height:190px;border-radius:0"></div>
      <div class="white-top" style="height:118px"></div>
      <div class="question" style="top:44px">Is it required?</div>
      <div class="check-row" style="top:142px"><div class="check-box"></div><span>No</span></div>
      <div class="check-row" style="top:185px"><div class="check-box"></div><span>Yes, but I do not have a file to upload</span></div>
      <div class="check-row" style="top:228px"><div class="check-box"><svg viewBox="0 0 28 28"><circle cx="14" cy="14" r="11.5" fill="none" stroke="var(--navy)" stroke-width="2.4"/><path d="M8 14 L13 19 L25 5" fill="none" stroke="var(--navy)" stroke-width="2.8" stroke-linecap="round" stroke-linejoin="round"/></svg></div><span>Yes, and I have a file to upload</span></div>
    </div>

    <div class="next-btn" style="top:610px">NEXT</div>
  </section>

</div>
</body>
</html>
```